Brisk Mark Lab atendeu e superou minhas expectativas. Usando os canais oferecidos, tive a possibilidade de atingir com relação à logomarca de nossa empresa.

```html
<!DOCTYPE html>
<html lang="pt-BR">
<head>
<meta charset="utf-8">
<title>Freefall Academy — Cartão de visita</title>
<link rel="stylesheet" href="https://fonts.googleapis.com/css2?family=Roboto:wght@400;500;700&display=swap">
<style>
  :root{
    --backdrop:#d9d9d9;
    --card-dark:#2b2b2b;
    --card-dark-edge:#1f1f1f;
    --card-light:#ffffff;
    --gold:#b68f3e;
    --silver:#c9c9c9;
    --ink:#3a3a3a;
  }
  *{margin:0;padding:0;box-sizing:border-box}
  html,body{width:1200px;height:1200px;overflow:hidden}
  body{
    background:var(--backdrop);
    display:flex;align-items:center;justify-content:center;
    font-family:"Roboto",Arial,sans-serif;
  }
  .business-card{
    width:900px;height:514px;border-radius:30px;overflow:hidden;
    background:var(--card-light);
    display:flex;flex-direction:column;
    box-shadow:0 20px 40px rgba(0,0,0,.18);
  }
  .card-header{
    height:250px;
    background:linear-gradient(180deg,var(--card-dark) 0%,var(--card-dark-edge) 100%);
    display:flex;align-items:center;padding-left:80px;gap:34px;
  }
  .brand-dot{
    width:120px;height:120px;border-radius:50%;
    background:var(--silver);flex:none;
  }
  .brand-name{
    color:var(--gold);font-weight:700;font-size:50px;line-height:1;letter-spacing:1px;
  }
  .brand-tagline{
    color:var(--silver);font-weight:400;font-size:17px;margin-top:14px;letter-spacing:.5px;
  }
  .gold-rule{height:6px;background:var(--gold)}
  .card-body{
    flex:1;padding:34px 80px 0;display:flex;flex-direction:column;
  }
  .contact-grid{display:grid;grid-template-columns:1fr 1fr;column-gap:40px;row-gap:18px}
  .contact-item{display:flex;align-items:flex-start;gap:14px;font-size:17px;color:var(--ink);line-height:1.35}
  .contact-icon{width:24px;height:24px;flex:none}
  .website{
    margin-top:auto;margin-bottom:30px;text-align:right;
    font-size:30px;font-weight:700;color:var(--gold);letter-spacing:.5px;
  }
  .bottom-rule{height:6px;background:var(--gold)}
</style>
</head>
<body>
  <article class="business-card">
    <header class="card-header">
      <span class="brand-dot"></span>
      <div class="brand-text">
        <div class="brand-name">Freefall Academy</div>
        <div class="brand-tagline">Escola de paraquedismo e queda livre</div>
      </div>
    </header>
    <div class="gold-rule"></div>
    <section class="card-body">
      <div class="contact-grid">
        <div class="contact-item">
          <svg class="contact-icon" viewBox="0 0 24 24"><circle cx="12" cy="12" r="12" fill="var(--gold)"/><circle cx="12" cy="12" r="4" fill="#fff"/></svg>
          <span>social.freefallacademy.com</span>
        </div>
        <div class="contact-item">
          <svg class="contact-icon" viewBox="0 0 24 24"><circle cx="12" cy="12" r="12" fill="var(--gold)"/><rect x="6" y="8" width="12" height="8" fill="none" stroke="#fff" stroke-width="1.6"/><path d="M6 8l6 5 6-5" fill="none" stroke="#fff" stroke-width="1.6"/></svg>
          <span>contato@freefallacademy.com</span>
        </div>
        <div class="contact-item">
          <svg class="contact-icon" viewBox="0 0 24 24"><circle cx="12" cy="12" r="12" fill="var(--gold)"/><path d="M8.5 6.5l2 2-1.3 1.6a7 7 0 0 0 4.7 4.7l1.6-1.3 2 2-1.5 1.8c-4.5-.3-8.8-4.6-9.1-9.1z" fill="#fff"/></svg>
          <span>tel 00000.0000 / 00000.0000</span>
        </div>
        <div class="contact-item">
          <svg class="contact-icon" viewBox="0 0 24 24"><circle cx="12" cy="12" r="12" fill="var(--gold)"/><path d="M12 5a4.5 4.5 0 0 0-4.5 4.5C7.5 13 12 19 12 19s4.5-6 4.5-9.5A4.5 4.5 0 0 0 12 5z" fill="#fff"/><circle cx="12" cy="9.5" r="1.6" fill="var(--gold)"/></svg>
          <span>End. completo do Bairro<br>CEP 0000-0000 - Cidade UF</span>
        </div>
      </div>
      <div class="website">www.freefallacademy.com</div>
    </section>
    <div class="bottom-rule"></div>
  </article>
</body>
</html>
```